依頼概要
・依頼の目的/概要
人生100年時代に、認知症や介護予防・改善に役立つ、美顔心療ワークショップの表紙デザインをお願いします。

・本の内容
高齢者の皆さんを抱えた、娘さん世代、ソーシャルビジネスとして取り組みたい女性、人の役に立ちたい・介護や医療関係者のスキルアップとして、心を癒すスキンタッチケアとしての美顔心療ワークショップを知って頂き、その効果を実例等で理解する事で、実践してみたくなる内容にしています。またお仕事としても、ボランティアとしても活躍できるセラピストの役割や募集にもふれています。
美顔心療ワークショップがどんなものか?!やるとどんな効果がきたいできるのか?!に、研究データーと実際の実例を交えて説明・解説した本です。

・デザイン要望
美容で心が癒される事が、伝わるようなイメージと解説でもあるので、美顔心療ワークショップのバイブルみたいな感じでしょうか?!(イメージカラーは、ピンクです。http://tkvb.or.jp tkvb-sora.com 色の感じです、参考資料)
もちろん、デザイナーさんのセンスにお任せします。

その他何かご不明な点がございましたら、お気軽にご質問ください。
よろしくお願いいたします。
■ 選んだ理由

認知症や介護の予防・改善を目指した療法ですので、見た方が、明るく安心し、そして楽しみになるイメージが持てるデザインを選びました。特に当選したものは、高齢者と若者が一緒に映る写真の印象が、表題のワークショップのイメージに繋がるということが、一番の選定理由です。

■ 提案者全員のお礼・コメント

素晴らしい表紙のデザインの応募をいただき、本当に感謝しています。
選定は、本当に悩みました。いくつも表紙にしたい作品がありました。出して頂いた作品が、教科書的と、読み物的な提案を頂いたように思います。皆さん素晴らしかったのですが、今回は親しみやすさを重視させて頂きました。特に最初に応募して頂いた、pelmiさんの表紙には、私の言いたい事が網羅されていて、良かったです。が、今回のテーマを考えて、残念ながら選定致しませんでした。
次の機会に皆様とお仕事ができれば、嬉しいです。ありがとうございました。

```html
<!DOCTYPE html>
<html lang="ja">
<head>
<meta charset="utf-8">
<title>美顔心療ワークショップ 表紙</title>
<link href="https://fonts.googleapis.com/css2?family=M+PLUS+Rounded+1c:wght@500;700;800&family=Kosugi+Maru&family=Dancing+Script:wght@700&display=swap" rel="stylesheet">
<style>
  :root {
    --pink: #e8578a;
    --pink-deep: #d83f76;
    --pink-pale: #fde6ee;
    --pink-soft: #f9c9da;
    --ink: #4a4a4a;
    --white: #ffffff;
    --accent-purple: #a15bc5;
    --accent-green: #79c04a;
  }
  html, body { margin: 0; padding: 0; overflow: hidden; }
  body { width: 750px; height: 1200px; }
  .cover {
    position: relative;
    width: 750px;
    height: 1200px;
    overflow: hidden;
    background: linear-gradient(180deg, var(--pink-pale) 0%, #fff5f8 22%, var(--white) 40%, var(--white) 62%, #fff3f7 80%, var(--pink-pale) 100%);
    font-family: "M PLUS Rounded 1c", "Kosugi Maru", sans-serif;
    color: var(--ink);
  }
  .frame {
    position: absolute;
    inset: 14px;
    border: 3px solid var(--pink-soft);
    border-radius: 6px;
  }
  .lead {
    position: absolute;
    top: 78px;
    left: 0;
    width: 100%;
    text-align: center;
    font-weight: 700;
    line-height: 1.3;
  }
  .lead .line1 { font-size: 46px; }
  .lead .line2 { font-size: 50px; }
  .lead .hl { color: var(--pink); }
  .title {
    position: absolute;
    top: 228px;
    left: 0;
    width: 100%;
    margin: 0;
    text-align: center;
    font-weight: 800;
    font-size: 146px;
    line-height: 1.02;
    letter-spacing: 6px;
  }
  .title .mark-purple { color: var(--accent-purple); }
  .title .mark-green { color: var(--accent-green); }
  .ribbon {
    position: absolute;
    top: 530px;
    left: 158px;
    width: 440px;
    height: 64px;
  }
  .ribbon svg { position: absolute; inset: 0; }
  .ribbon-text {
    position: absolute;
    inset: 0;
    display: flex;
    align-items: center;
    justify-content: center;
    color: var(--white);
    font-weight: 800;
    font-size: 40px;
    letter-spacing: 3px;
  }
  .author {
    position: absolute;
    top: 610px;
    left: 0;
    width: 100%;
    text-align: center;
    font-weight: 700;
    font-size: 42px;
    letter-spacing: 6px;
  }
  .illustration {
    position: absolute;
    left: 290px;
    top: 712px;
    width: 430px;
    height: 470px;
    border-radius: 48% 48% 12px 12px;
    background: radial-gradient(circle at 40% 45%, #fbd6e1 0%, #f6b9cf 45%, #fbe3ec 100%);
  }
  .bonus {
    position: absolute;
    left: 22px;
    top: 850px;
    width: 250px;
    height: 250px;
    border-radius: 50%;
    background: var(--white);
    border: 5px solid var(--pink);
    box-sizing: border-box;
    text-align: center;
    color: var(--pink-deep);
    font-weight: 800;
  }
  .bonus .b1 { margin-top: 34px; font-size: 34px; line-height: 1.15; }
  .bonus .b2 { font-size: 18px; color: var(--ink); margin-top: 10px; line-height: 1.4; font-weight: 700; }
  .bonus .b3 {
    font-family: "Dancing Script", cursive;
    font-size: 40px;
    color: var(--pink);
    margin-top: 4px;
  }
</style>
</head>
<body>
<div class="cover">
  <div class="frame"></div>

  <div class="lead">
    <div class="line1">笑顔をひらき、</div>
    <div class="line2"><span class="hl">毎日</span>を彩る</div>
  </div>

  <h1 class="title">
    <div>美<span class="mark-purple">顔</span></div>
    <div>心<span class="mark-green">療</span></div>
  </h1>

  <div class="ribbon">
    <svg viewBox="0 0 440 64" width="440" height="64" aria-hidden="true">
      <polygon points="0,8 30,8 22,32 30,56 0,56 14,32" fill="var(--pink-deep)"/>
      <polygon points="440,8 410,8 418,32 410,56 440,56 426,32" fill="var(--pink-deep)"/>
      <rect x="24" y="0" width="392" height="64" rx="6" fill="var(--pink)"/>
    </svg>
    <div class="ribbon-text">ワークショップ</div>
  </div>

  <div class="author">花野美咲</div>

  <div class="illustration" role="img" aria-label="イラスト：若い女性が高齢の女性にメイクをしている様子"></div>

  <div class="bonus">
    <div class="b1">読者限定<br>2大特典</div>
    <div class="b2">「笑顔ストレッチ」<br>「手のひら温もりケア」</div>
    <div class="b3">Present</div>
  </div>
</div>
</body>
</html>
```